International Dispute Resolution Magazine

We are issuing a Magazine on International Arbitration for Chinese lawyers. It will be in HTML format.

Kelvatrin is a consulting firm bridging the gap between Chinese and international arbitration. The newsletter aims at educating Chinese lawyers about international arbitration and promote Kelvatrin as a firm actively sharing know-how and experience.

The 1first uploaded document (Kelvatrin Magazine Complete Content) contains the full content of the Magazine. The end product - newsletter is going to be published in Chinese Mandarin.

It is important that the design of the Magazine is in line with our style and our corporate identity. The attachment 2 and 3 are examples of flyers promoting our past events. Please refer to them while working on the design.

Our new logo which we would like to be in the Magazine is in the attachment 4.

We would like to get a structure design as well as flyer design.

Target Market(s)

Chinese legal and business community. After we have the design, the content of the Magazine will be translated into Chinese Mandarin.

Industry/Entity Type

Events

Requirements
Must have
• The Magazine must adhere to our corporate identity and have our new logo. As an example, please refer to the attachments where our previous events are advertised.

```html
<!DOCTYPE html>
<html lang="en">
<head>
<meta charset="utf-8">
<title>Kelvatrin – Magazine on International Arbitration</title>
<link href="https://fonts.googleapis.com/css2?family=Montserrat:wght@700;800&family=Noto+Serif:ital,wght@0,400;1,400;1,700&display=swap" rel="stylesheet">
<style>
  :root {
    --backdrop: #9b9b9b;
    --paper: #f7f7f7;
    --ink: #1c1c1c;
    --accent-orange: #e8731e;
    --accent-teal: #17678a;
  }
  * { box-sizing: border-box; margin: 0; padding: 0; }
  html, body { width: 1200px; height: 851px; overflow: hidden; }
  body {
    background: var(--backdrop);
    font-family: "Noto Serif", Georgia, serif;
    color: var(--ink);
  }
  .spread {
    position: absolute;
    left: 40px; top: 30px;
    width: 1120px; height: 791px;
    display: flex;
  }
  .page {
    position: relative;
    width: 560px; height: 791px;
    background: var(--paper);
    overflow: hidden;
  }
  .page--left { border-right: 1px solid #d4d4d4; }
  .page-header {
    position: absolute; top: 26px; left: 32px; right: 32px;
    display: flex; align-items: center; gap: 26px;
    font-family: "Montserrat", Arial, sans-serif;
  }
  .page--right .page-header { justify-content: flex-start; }
  .issue-line {
    color: var(--accent-orange);
    font-weight: 800; font-size: 11px; letter-spacing: 0.6px;
  }
  .brand {
    font-family: "Montserrat", Arial, sans-serif;
    font-weight: 800; font-size: 19px;
    color: var(--accent-teal);
    letter-spacing: -0.3px;
  }
  .page--left .brand { margin-left: 40px; }
  .article {
    position: absolute; top: 78px; left: 38px; right: 38px; bottom: 56px;
    font-size: 9.6px; line-height: 12.4px;
    text-align: justify; hyphens: auto;
  }
  .page--right .article { left: 40px; right: 36px; top: 74px; }
  .article p { margin-bottom: 8px; }
  .article .question { font-style: italic; margin-bottom: 8px; }
  .page-footer {
    position: absolute; bottom: 18px; left: 0; right: 0; height: 20px;
    display: flex; align-items: center;
    font-family: "Montserrat", Arial, sans-serif;
  }
  .page--right .page-footer { justify-content: flex-end; }
  .folio {
    width: 48px; height: 20px; background: var(--accent-teal);
    color: #fff; font-weight: 700; font-size: 10px;
    display: flex; align-items: center; justify-content: center;
  }
  .page--left .folio { clip-path: polygon(0 0, 100% 0, 82% 100%, 0 100%); padding-right: 6px; }
  .page--right .folio { clip-path: polygon(18% 0, 100% 0, 100% 100%, 0 100%); padding-left: 6px; }
  .magazine-title {
    color: var(--accent-orange); font-weight: 700; font-size: 9.5px;
    letter-spacing: 0.3px; margin: 0 10px;
  }
</style>
</head>
<body>
<main class="spread">
  <section class="page page--left">
    <header class="page-header">
      <span class="issue-line">VOL I - NO. 1 | OCTOBER 21, 2014</span>
      <span class="brand">Kelvatrin</span>
    </header>
    <article class="article">
      <p class="question">3. What are the lawyers' and the arbitrators' share of responsibility in this growing costliness?</p>
      <p>In a way both lawyers and arbitrators are responsible for this. I mainly sit as an arbitrator so I do not want to blame solely the lawyers for that. I think that arbitrators also have their share in this responsibility. The lawyers' responsibility can be seen in the fact that in many cases there is a tendency to over-lawyer arbitrations and to drag the length of the proceedings and to include every imaginable step in the proceedings. There is a reason for it: the lawyers represent their clients, they have instructions; the lawyers representing the claimant want to win the case and the respondent's lawyers do not want to lose their case, so there is a reason for building up such solid teams and for seeing to it that all procedural rights can be exercised. You can't have it all, I mean either you fight like in a litigation, at this price or you find more flexible solutions and then you can reduce the costs.</p>
      <p>The arbitrators share this responsibility as they often let it go and do not intervene in order to keep the costs under control. I think arbitrators should be more robust and in the interest of parties they should make proposals and develop techniques to reduce the costs.</p>
      <p class="question">4. As concerns lawyers, sometimes the cost of legal representation gets out of proportion with the economic value of the dispute. In one of your articles you mention a case where the claim was about 1.5 mln euro, while the costs of representation of both parties amounted to over 0.5 mln euro. What is the best way to remedy such a situation?</p>
      <p>One solution is to agree on a sole arbitrator. That would reduce fees of arbitrators. In addition, in such a case both sides should see to it that the lawyers' team remains small. If the case involves a relatively modest amount of money, it should be feasible to deal with the case with 1 partner and one or two assistants, instead of sending 5 people on the case. I think one must look at the size of the case: value of the case, legal complexity, and then adopt the procedure to these parameters. If the amount is low, relatively speaking, it is completely unacceptable for the parties that the cost of representation amounts to more than a third of the value at stake.</p>
      <p class="question">5. As an arbitrator, what are 2-3 measures you always recommend to control costs?</p>
      <p>In all cases I would recommend to the parties to send representatives, i.e. people from the company's management, to the case management conference, so that the arbitrators and council meet and agree on the proceedings. This is quite helpful because the company representatives would be directly involved in the discussion about the duration of the proceedings. In such situations, the tribunal would be reminded that its duty is to render the award quickly as the rules provide that it should be done within a certain deadline.</p>
      <p>In GAC Proceedings I would recommend to refer the Techniques to Control Costs in Arbitration. This is a quite useful paper produced by the GAC. You can refer to it in the presence of the parties. You can tell them "we fulfill the duty to see to it that the proceedings are carried out efficiently and at reasonable costs. Here are some recommendations, we will take them into account and they should be also taken seriously by the parties.</p>
      <p>It has been recently more and more suggested and also put to practice to have a midstream case management conference between the initial case management conference and the hearing, precisely when the parties submitted the full first briefs, meaning the full statement of claim and the full statement of defense. For example, Noel Karpin launched this idea called</p>
    </article>
    <footer class="page-footer">
      <span class="folio">9</span>
      <span class="magazine-title">MAGAZINE ON INTERNATIONAL ARBITRATION</span>
    </footer>
  </section>

  <section class="page page--right">
    <header class="page-header">
      <span class="brand">Kelvatrin</span>
      <span class="issue-line">VOL I - NO. 1 | OCTOBER 21, 2014</span>
    </header>
    <article class="article">
      <p>the "Karpin openings", to invite councils at such a midstream case management conference to orally plead their cases based on what has been submitted so far and then engage into a sort of dialogue with the arbitrators and then the arbitrators can point out to what they think are the most relevant issues to be covered in the second round of the submissions. I very much like this idea and quite a few of my colleagues like it too. We had some discussion recently in a conference and it was interesting to see that not only lawyers from civil law countries but also common law practitioners are interested in that idea. I feel that the time spent between the initial time management conference and the hearing has become too long. As a rule, it is 1,5 year during which there is no real interaction between the parties and the tribunal. I think that in many cases it would be helpful in order to streamline the proceedings and to focus on relevant issues if halfway there was such interaction between parties, councils and the tribunal.</p>
      <p class="question">6. What is the role of arbitral institutions in controlling costs of arbitral proceedings?</p>
      <p>Their role is limited. They have only direct control regarding the fees of the institution and of the arbitrators. They can monitor the development of the case to adapt the advances on costs, based on the progress of the case, on the intensity and on the value at stake, and to see to it that arbitrators' fees may be reduced if the arbitrators do not deliver the award in due time; or to the contrary, that an efficient tribunal is rewarded in terms of fees.</p>
      <p class="question">7. What is your experience with "step-clauses", i.e. clauses that contemplate mediation or early neutral evaluation prior to the commencement of arbitration? Do they decrease or increase the costs of the proceedings?</p>
      <p>It is an interesting question and I have mixed experience with such clauses. Generally, if a clause provides for mandatory mediation my experience shows that if the parties have to go to mediation, they do it not whole-heartedly but because they have to do it. So they see it as an unwelcomed step in the procedure. In my experience, mediation is more successful if it is agreed ad hoc, i.e. if both parties think that they should attend to find a compromise via mediation, it will be more successful than imposed mediation. Of course, mediation adds to costs proceedings. I am not against mediation, mediation has its place, but it can only work if the parties really desire it, if they think "well, let's at least try that". To impose mediation on parties would be rarely successful.</p>
    </article>
    <footer class="page-footer">
      <span class="magazine-title">MAGAZINE ON INTERNATIONAL ARBITRATION</span>
      <span class="folio">10</span>
    </footer>
  </section>
</main>
</body>
</html>
```